Prairie Wellhead Gear Depot Web Template
Oilfield Equipment web site development
Also #76 shows off shore ...........
thanks,
CraftyPixelSmith
ZorbIx
Hi PH,
please feel free to let me know the required changes so that your expectations are met.
Awaiting for your kind feedback
Designers: Thank you for all of your submitted drafts. The few that remain on the page are what I am look for in terms of a home page. Please keep the designs coming, I really appreciate all of your hard work. Everything looks great so far. I would like to keep the images land related. Ex: no offshore rig pictures. Our targeted area is for onshore production not offshore.
DRAFT # 9 IS AN EXAMPLE OF THE TYPE OF HOME PAGE TEMPLATE I AM LOOKING FOR.
NOTE: PRAIRIE WELLHEAD GEAR DEPOT IS SINGULAR. THE WORD EQUIPMENT SHOULD NEVER HAVE AN "S" AT THE END OF THE WORD. EX: DRAFTS # 4-9 SHOULD NOT HAVE A "S" AT THE END OF EQUIPMENT IN "WELCOME TO PRAIRIE WELLHEAD GEAR(S) DEPOT". ALSO IN "FEATURED EQUIPMENT(S).
Just a thought.....I would like to have the ability to show the current crude oil prices shown in a graph that is updated daily. Ex: www.barrel-rates-demo.net
I would like the logo to be larger than in Drafts #1-3.
Icon "equipment for sale" is singular and not plural
The website will be strictly to advertise equipment for sale and customers will not be able to purchase equipment through a shopping cart.
In drafts # 1-3, lets change "featured articles" to "featured equipment".
Website template should have 5 icons.
1st icon: home
2nd icon: about us
3rd icon: services
4th icon: equipment for sale
5th icon: contact us
Quick reminder:
I would like to keep “offshore rig pictures” off the home page. The equipment that is being sold is for the oil and gas industry but mainly used onshore in the production side of things.
I like the clean lines on draft #1. Draft # 1 is definitely on the right track. Keep up the good work. I look forward to seeing everyone’s drafts.

```html
<!DOCTYPE html>
<html lang="en">
<head>
<meta charset="utf-8">
<title>Prairie Wellhead Gear Depot</title>
<link href="https://fonts.googleapis.com/css2?family=Arimo:wght@400;700&display=swap" rel="stylesheet">
<style>
:root{
  --red:#d0121b;
  --red-dark:#8e0a10;
  --ink:#1b1b1b;
  --grey:#5a5a5a;
  --light:#efefef;
  --line:#d5d5d5;
  --white:#ffffff;
  --tile:#2f64a8;
}
*{box-sizing:border-box;margin:0;padding:0}
html,body{width:1200px;height:1085px;overflow:hidden}
body{font-family:"Arimo",Arial,sans-serif;background:linear-gradient(#fafafa,#e6e6e6);color:var(--ink);position:relative}
.abs{position:absolute}
/* header */
.brand{left:155px;top:32px;display:flex;align-items:center;gap:14px}
.brand-mark{width:90px;height:90px;border-radius:50%;background:var(--red)}
.brand-name{font-size:64px;font-weight:700;letter-spacing:1px;line-height:1}
.brand-sub{font-size:14px;font-weight:700;color:var(--red);letter-spacing:.5px;margin-top:4px}
.call{left:830px;top:80px;display:flex;align-items:center;gap:10px;font-size:22px;color:var(--ink)}
.call svg{width:34px;height:34px}
/* nav */
.nav{left:155px;top:142px;width:970px;height:40px;background:linear-gradient(#2b2b2b,#0f0f0f);border-bottom:3px solid var(--red);display:flex;align-items:center}
.nav a{color:var(--white);text-decoration:none;font-size:15px;padding:0 22px;height:100%;display:flex;align-items:center}
.nav a.active{background:linear-gradient(var(--red),var(--red-dark))}
.search{margin-left:auto;margin-right:14px;width:210px;height:24px;border-radius:12px;background:var(--white);font-size:12px;color:#999;display:flex;align-items:center;justify-content:space-between;padding:0 10px}
/* slider */
.slider{left:160px;top:192px;width:960px;height:340px;background:linear-gradient(120deg,#3a3f44,#15181b);overflow:hidden;border:1px solid #111}
.slide-photo{position:absolute;left:0;top:0;width:480px;height:300px;background:linear-gradient(#aab7c4,#6b7a88 60%,#3d4650)}
.slide-copy{position:absolute;left:510px;top:70px;width:420px;color:var(--white)}
.slide-copy h1{font-size:30px;line-height:1.2;font-weight:700}
.slide-copy p{font-size:13px;color:#d6d6d6;margin-top:10px;line-height:1.5}
.btn-dark{position:absolute;right:22px;bottom:66px;background:#111;color:var(--white);font-size:14px;padding:7px 16px;border-radius:3px}
.swoosh{position:absolute;left:0;bottom:0;width:960px;height:60px}
.arrow{top:330px;width:36px;height:56px;background:var(--red);display:flex;align-items:center;justify-content:center}
/* columns */
.col{top:560px;height:370px;background:var(--white);border:1px solid var(--line);border-radius:4px}
.col-head{height:36px;background:linear-gradient(var(--red),var(--red-dark));color:var(--white);font-size:15px;display:flex;align-items:center;gap:10px;padding-left:12px;border-radius:4px 4px 0 0}
.col-head i{width:22px;height:22px;border-radius:50%;background:var(--white);display:block}
.col-body{padding:12px 14px;font-size:11.5px;line-height:1.45;color:var(--grey)}
.col-body p+p{margin-top:10px}
.col-body b{color:var(--ink)}
.service{display:flex;gap:8px;margin-bottom:14px}
.service-thumb{width:52px;height:44px;flex:none;background:linear-gradient(#7d8a96,#3b434b)}
.feature{list-style:none}
.feature li{font-size:12.5px;color:var(--ink);padding:4px 0 4px 16px;position:relative}
.feature li:before{content:"";position:absolute;left:2px;top:8px;border-left:6px solid var(--red);border-top:4px solid transparent;border-bottom:4px solid transparent}
.btn-more{position:absolute;right:12px;bottom:12px;background:var(--red);color:var(--white);font-size:12px;padding:5px 14px;border-radius:3px}
/* clients */
.clients{left:158px;top:955px;width:965px;height:78px;background:var(--white);border:1px solid var(--line);border-radius:4px;display:flex;align-items:center;overflow:hidden}
.clients-label{flex:none;height:100%;width:150px;background:linear-gradient(#333,#0e0e0e);color:var(--white);font-size:17px;display:flex;align-items:center;gap:8px;padding-left:14px}
.clients-label i{width:24px;height:24px;border-radius:50%;background:var(--red);display:block}
.client{flex:1;min-width:0;text-align:center;font-size:13px;font-weight:700;color:var(--grey);border-left:1px solid var(--line);white-space:nowrap}
/* footer */
.footer{left:160px;top:1042px;width:960px;height:36px;display:flex;align-items:center}
.footer-links{font-size:10px;color:var(--grey);line-height:1.6}
.follow{margin-left:auto;display:flex;align-items:center;gap:8px;font-size:17px;color:var(--grey)}
.follow .soc{width:34px;height:34px;background:var(--tile);border-radius:4px;color:var(--white);font-size:8px;display:flex;align-items:center;justify-content:center}
.foot-brand{margin-left:40px;font-size:24px;font-weight:700;color:var(--grey);display:flex;align-items:center;gap:8px}
.foot-brand i{width:30px;height:30px;border-radius:50%;background:#9a9a9a;display:block}
</style>
</head>
<body>
<header>
  <div class="abs brand">
    <span class="brand-mark"></span>
    <div><div class="brand-name">PRAIRIE</div><div class="brand-sub">WELLHEAD GEAR DEPOT</div></div>
  </div>
  <div class="abs call">
    <svg viewBox="0 0 24 24"><circle cx="12" cy="12" r="12" fill="#1b1b1b"/><path d="M8 6l2 0 1 3-1.5 1a7 7 0 0 0 4.5 4.5l1-1.5 3 1v2a1.5 1.5 0 0 1-1.5 1.5A10 10 0 0 1 6.5 7.5 1.5 1.5 0 0 1 8 6z" fill="#fff"/></svg>
    CALL NOW: 000-000-0000
  </div>
  <nav class="abs nav">
    <a class="active">HOME</a><a>ABOUT US</a><a>SERVICES</a><a>EQUIPMENT</a><a>CONTACT US</a>
    <div class="search">search <svg width="12" height="12" viewBox="0 0 12 12"><circle cx="5" cy="5" r="3.5" stroke="#888" fill="none" stroke-width="1.5"/><path d="M8 8l3 3" stroke="#888" stroke-width="1.5"/></svg></div>
  </nav>
</header>

<section class="abs slider">
  <div class="slide-photo" role="img" aria-label="Onshore oil pump jack against an overcast sky"></div>
  <div class="slide-copy">
    <h1>Lorem ipsum dolor sit amet, consectetudipisg elit.</h1>
    <p>Pellentesque interdum augue vitae leo adipiscing nec tempus nisl semper. Integer pharetra, velit quis elementum semper.</p>
  </div>
  <svg class="swoosh" viewBox="0 0 960 60" preserveAspectRatio="none"><path d="M0 40 Q300 0 960 30 L960 60 L0 60Z" fill="#d0121b"/><path d="M0 50 Q320 18 960 44 L960 60 L0 60Z" fill="#1a1a1a"/></svg>
  <span class="btn-dark">Read More</span>
</section>
<div class="abs arrow" style="left:146px"><svg width="14" height="20"><path d="M12 2L3 10l9 8" stroke="#fff" stroke-width="3" fill="none"/></svg></div>
<div class="abs arrow" style="left:1092px"><svg width="14" height="20"><path d="M2 2l9 8-9 8" stroke="#fff" stroke-width="3" fill="none"/></svg></div>

<section class="abs col" style="left:160px;width:290px">
  <div class="col-head"><i></i>WELCOME TO PRAIRIE</div>
  <div class="col-body">
    <p><b>Donec turpis odio, lobortis sed malesuada</b> id, venenatis ut justo. Vestibulum ante ipsum primis in faucibus orci luctus et ultrices posuere cubilia Curae; Suspendisse malesuada viverra porttitor. Suspendisse potenti. <b>Nulla</b> risus dui, volutpat ac convallis nec, sodales nec felis.</p>
    <p>Donec turpis odio, lobortis sed malesuada id, venenatis ut justo. Vestibulum ante ipsum primis in faucibus orci luctus et ultrices posuere cubilia Curae; Suspendisse malesuada viverra porttitor. Suspendisse potenti. Nulla risus dui, volutpat ac convallis nec, sodales nec felis.</p>
  </div>
  <span class="btn-more">More</span>
</section>

<section class="abs col" style="left:462px;width:295px">
  <div class="col-head"><i></i>OUR SERVICES</div>
  <div class="col-body">
    <div class="service"><div class="service-thumb" role="img" aria-label="Drilling rig on land"></div><div><b>Donec turpis odio, lobortis sed malesuada id, venenatis ut justo.</b> Vestibulum ante ipsum primis in faucibus orci luctus et.</div></div>
    <div class="service"><div class="service-thumb" role="img" aria-label="Wellhead valves"></div><div><b>Donec turpis odio, lobortis sed malesuada id, venenatis ut justo.</b> Vestibulum ante ipsum primis in faucibus orci luctus et.</div></div>
    <div class="service"><div class="service-thumb" role="img" aria-label="Equipment yard"></div><div><b>Donec turpis odio, lobortis sed malesuada id, venenatis ut justo.</b> Vestibulum ante ipsum primis in faucibus orci luctus et.</div></div>
  </div>
  <span class="btn-more">More</span>
</section>

<section class="abs col" style="left:770px;width:340px">
  <div class="col-head"><i></i>FEATURED EQUIPMENT</div>
  <div class="col-body">
    <ul class="feature">
      <li>Rig Automation &amp; Control</li><li>Drilling &amp; Monitoring</li><li>Engines &amp; Generators</li><li>Ac &amp; DC Drawworks</li><li>Deepwater Drilling System</li><li>All Capital Drilling Equipment</li><li>Boilers</li><li>Casing Towers</li><li>Corrosion Inspection Tools</li><li>Turbines, Generator and transformers</li>
    </ul>
  </div>
  <span class="btn-more">More</span>
</section>

<section class="abs clients">
  <div class="clients-label"><i></i>Our Clients</div>
  <span class="client">Harlow Ridge</span><span class="client">Tamsen Works</span><span class="client">Quillbrook</span><span class="client">Oakhaven Co</span><span class="client">Brantley Group</span><span class="client">Vellmoor</span><span class="client">Ashgrove Ltd</span>
</section>

<footer class="abs footer">
  <div class="footer-links">Home | About Us | Services | Contact Us | Privacy Policy | Disclaimer | Site Map<br>Copyright © 2011 Prairie Wellhead Gear Depot All Rights Reserved</div>
  <div class="follow">Follow Us <span class="soc">Vinelo</span><span class="soc">Pebblo</span><span class="soc">Wirra</span></div>
  <div class="foot-brand"><i></i>PRAIRIE</div>
</footer>
</body>
</html>
```